Stationery Design Project - Professional Training Company

Full set of statinery in PDF and format that can be given to the printers

Letterhead
Business cards x 3
Compliments slip
Envelope
Updates

Many thanks for all your contributions, the quality of the designs is amazing.

Thank you all so much for your contribution to this project, I am very impressed with the designs and choice of designs, you are all clearly very talented individuals.

I hope to be making a decision on the final choice this evening UAE time.

Best regards and again thank you so much

Gordon

I would like to take this opportunity to thank you all for your contributions, I have been very impressed with each of the designs submitted.

I will shortly go back and give each of you a personal rating on each of your designs.

Again thank you all so much for your efforts

Best Regards

Gordon

Target Market(s)

We are a training company that provides IT training for Medical and Professional Staff, we train professional adults

Industry/Entity Type

Business

Requirements
Must have
• The letterhead and compliments slip must have at the bottom of the page:-

Bright Ledger Pathways LLP operates as a limited liability partnership registered in England and Wales (with registered number OC702614)

Business Cards are to be made up for three people (details of those to be provided after appoval of design but are included in this project) and should contain:

Name
Title
Telephone
email
Address: P.O. Box 418263 Dubai UAE
web address: www.brightledgerpathways.example
Nice to have
• Very clean and professional looking
Should not have
• No look to busy or ovr crowded

```html
<!DOCTYPE html>
<html lang="en">
<head>
<meta charset="utf-8">
<title>Bright Ledger Pathways LLP – Compliments Slips</title>
<link rel="stylesheet" href="https://fonts.googleapis.com/css2?family=Didact+Gothic&family=Questrial&display=swap">
<style>
  :root {
    --backdrop: #4b4b4b;
    --paper: #ffffff;
    --ink: #1c0d1c;
    --plum: #7a2a6e;
    --plum-light: #a44a96;
    --plum-dark: #4a1040;
    --leaf: #2e7d12;
    --leaf-light: #7cc22a;
    --legal-grey: #8a8a8a;
    --rule: #a8a8a8;
  }
  * { box-sizing: border-box; margin: 0; padding: 0; }
  html, body { width: 1200px; height: 1000px; overflow: hidden; }
  body {
    background: var(--backdrop);
    position: relative;
    font-family: "Didact Gothic", "Century Gothic", sans-serif;
    color: var(--ink);
  }
  .slip {
    position: absolute;
    top: 118px;
    width: 364px;
    height: 772px;
    background: var(--paper);
    overflow: hidden;
  }
  .slip--side-band { left: 158px; }
  .slip--footer-band { left: 685px; }

  .side-band {
    position: absolute; left: 0; top: 0; width: 17px; height: 100%;
  }
  .side-band__plum {
    position: absolute; top: 0; left: 0; width: 100%; height: 562px;
    background: linear-gradient(180deg, var(--plum-light), var(--plum-dark));
  }
  .side-band__leaf {
    position: absolute; top: 564px; left: 0; width: 100%; bottom: 0;
    background: linear-gradient(180deg, #1f5a0c, var(--leaf-light));
  }

  .brand {
    position: absolute; left: 50px; top: 42px;
  }
  .brand__mark {
    width: 64px; height: 64px; border-radius: 50%;
    background: var(--plum);
    margin-bottom: 26px;
  }
  .brand__name {
    font-family: "Didact Gothic", "Century Gothic", sans-serif;
    font-size: 30px; line-height: 32px;
    color: var(--ink);
    letter-spacing: -0.5px;
  }

  .compliments {
    position: absolute; left: 50px; right: 20px;
  }
  .slip--side-band .compliments { top: 616px; }
  .slip--footer-band .compliments { top: 378px; left: 28px; }

  .compliments__title {
    font-family: "Questrial", "Century Gothic", sans-serif;
    font-size: 34px; font-weight: 400; line-height: 40px;
    color: var(--ink);
    white-space: nowrap;
  }
  .compliments__title em { font-style: normal; color: var(--plum); }

  .contact {
    margin-top: 14px;
    font-size: 11.5px; line-height: 14px;
    color: var(--ink);
  }
  .rule {
    height: 1px; background: var(--rule);
    margin: 10px 0 8px; width: 294px;
  }
  .legal {
    font-size: 11.5px; line-height: 13px;
    color: var(--legal-grey);
    width: 300px;
  }

  .footer-band {
    position: absolute; left: 0; right: 0; top: 537px; bottom: 0;
    background:
      radial-gradient(circle at 70% 10%, #8e3a83 0%, transparent 55%),
      linear-gradient(135deg, #6a1d5e 0%, #5a1450 55%, #3e0c38 100%);
  }
</style>
</head>
<body>

  <section class="slip slip--side-band">
    <div class="side-band">
      <div class="side-band__plum"></div>
      <div class="side-band__leaf"></div>
    </div>

    <div class="brand">
      <div class="brand__mark"></div>
      <p class="brand__name">Bright Ledger<br>Pathways LLP</p>
    </div>

    <div class="compliments">
      <h2 class="compliments__title">With <em>Compliments</em></h2>
      <p class="contact">P.O. Box 418263, Dubai UAE.&nbsp; Phone: +971 4 555 0182<br>www.brightledgerpathways.example</p>
      <div class="rule"></div>
      <p class="legal">Bright Ledger Pathways LLP operates as a limited liability partnership registered in England and Wales (with registered number OC702614)</p>
    </div>
  </section>

  <section class="slip slip--footer-band">
    <div class="brand" style="left:28px;">
      <div class="brand__mark"></div>
      <p class="brand__name">Bright Ledger<br>Pathways LLP</p>
    </div>

    <div class="compliments">
      <h2 class="compliments__title">With <em>Compliments</em></h2>
      <p class="contact">P.O. Box 418263, Dubai UAE.&nbsp; Phone: +971 4 555 0182<br>www.brightledgerpathways.example</p>
      <div class="rule"></div>
      <p class="legal">Bright Ledger Pathways LLP operates as a limited liability partnership registered in England and Wales (with registered number OC702614)</p>
    </div>

    <div class="footer-band" role="img" aria-label="Large plum brand decoration filling the lower band"></div>
  </section>

</body>
</html>
```